Tea standup pouch labels

Dear designers,
I need a minimalistic and modern label for my loose tea stand-up pouches (100, 250 and 500gm packs). The label should cover 70-80% of the pouch face (front and rear both).
The label will be 2 part label - Front and Rear side labels.
The labels should have a green background (Pantone Green C) with Golden or White or black colour text. Please either use the Golden logo or black logo to see which looks good with Pantone Green C background.
I am also attaching the content file and a few other files (Assam tea logo) to be used in the label.
The Assam tea logo should be small at the bottom left or right side of the front side. The logo should be dominant on the front page (some of the designs I received have small logo and big "100% single estate tea" and "Assam logo" as big characters on the front page which is not what I am looking for.

The font style should note simple Times new roman or Arial. It should look modern and should be something matching to the logo sentence 'Freshest possible' but should also not be in italics. Please refer to files Font style reference front and back for the style of font. Also use the same box space design on the rear - Content should be in White background; the rectangular box edges should be rounded and the border should be in dual colour - Golden and white or in black and white depending on the logo colour used (golden or black).

For the Rear page - headings could be in Golden colour or black colour depending on the logo colour you choose to use and the text can be in white colour i.e. Option 1 - Headings in golden colour and text in white colour; Option 2 - Heading in Black colour and text in white colour or any other combination that looks good - designer to decide.

Please let me know if you need any further information.

thanks,
Toral

```html
<!DOCTYPE html>
<html lang="en">
<head>
<meta charset="utf-8">
<title>Teavora – Front Pouch Label</title>
<link href="https://fonts.googleapis.com/css2?family=Josefin+Sans:wght@300;400&family=Dancing+Script:wght@500&display=swap" rel="stylesheet">
<style>
  :root {
    --backdrop: #e9efef;
    --label-green: #1d9a86;
    --label-green-deep: #17907c;
    --leaf-tint: #23a690;
    --gold: #c98f2c;
    --ink: #15201e;
    --white: #ffffff;
  }
  * { margin: 0; padding: 0; box-sizing: border-box; }
  html, body {
    width: 1200px; height: 1200px; overflow: hidden;
    background: var(--backdrop);
    font-family: "Josefin Sans", Arial, sans-serif;
  }
  .canvas { position: relative; width: 1200px; height: 1200px; }

  .front-label {
    position: absolute; left: 220px; top: 68px;
    width: 760px; height: 1064px;
    background: var(--label-green);
    overflow: hidden;
  }
  .leaf-pattern-area {
    position: absolute; inset: 0;
    background: radial-gradient(ellipse at 40% 45%, var(--leaf-tint) 0%, var(--label-green) 55%, var(--label-green-deep) 100%);
  }

  .estate-banner {
    position: absolute; left: 180px; top: 206px;
    width: 400px; height: 56px;
    background: var(--gold);
  }
  .estate-claim {
    position: absolute; left: 0; right: 0; top: 204px;
    text-align: center; color: var(--white);
    font-weight: 400; font-size: 34px; letter-spacing: 2px; line-height: 42px;
  }

  .brand-lockup {
    position: absolute; left: 0; right: 0; top: 430px;
    display: flex; flex-direction: column; align-items: center; gap: 28px;
  }
  .brand-mark-dot {
    width: 64px; height: 64px; border-radius: 50%;
    border: 4px solid var(--ink);
  }
  .brand-name {
    color: var(--ink); font-weight: 300;
    font-size: 92px; letter-spacing: 14px; line-height: 1;
    padding-left: 14px;
  }
  .brand-tagline {
    position: absolute; left: 0; right: 0; top: 780px;
    text-align: center; color: var(--ink);
    font-family: "Dancing Script", cursive; font-size: 36px;
  }

  .net-weight {
    position: absolute; left: 197px; width: 300px; top: 955px;
    text-align: center; color: var(--white);
    font-weight: 300; font-size: 28px; line-height: 40px;
  }

  .origin-badge {
    position: absolute; left: 505px; top: 882px;
  }
</style>
</head>
<body>
  <main class="canvas">
    <section class="front-label">
      <div class="leaf-pattern-area" role="img" aria-label="Faint tea leaf line pattern across the green label"></div>

      <div class="estate-banner" role="img" aria-label="Gold brush stroke behind the estate claim"></div>
      <p class="estate-claim">100% SINGLE<br>ESTATE TEA</p>

      <div class="brand-lockup">
        <div class="brand-mark-dot"></div>
        <h1 class="brand-name">TEAVORA</h1>
      </div>
      <p class="brand-tagline">freshest possible</p>

      <p class="net-weight">Net Wt<br>250g/8.82oz</p>

      <svg class="origin-badge" width="96" height="96" viewBox="0 0 96 96" role="img" aria-label="Tea origin certification badge">
        <circle cx="48" cy="48" r="46" fill="var(--white)" stroke="var(--ink)" stroke-width="3"/>
        <circle cx="48" cy="48" r="38" fill="none" stroke="var(--ink)" stroke-width="2"/>
      </svg>
    </section>
  </main>
</body>
</html>
```